Business Card for Business consulting practice

Need a design for a consultant business card. Simple and elegant.
I need the following information on the card:
Logo: (see uploaded file)
Company name: Callendry Advisory Group
Name: Noel Fardwick
Title: Managing Director - Aerospace and Defence
Phone #: 438-261-7083
e-mail: noel.fardwick@callendry.example
Website: www.callendry.example
Tagline: Proposals Management and Capture support for complex procurements

```html
<!DOCTYPE html>
<html lang="en">
<head>
<meta charset="utf-8">
<title>Callendry Advisory Group — Business Card</title>
<link rel="stylesheet" href="https://fonts.googleapis.com/css2?family=Cinzel:wght@600&family=Karla:wght@400;500&display=swap">
<style>
  :root {
    --bg: #e9ecef;
    --brand-blue: #1d93be;
    --accent-blue: #2aa0d2;
    --navy: #0e2940;
    --paper: #f7f8f8;
    --white: #ffffff;
  }
  * { box-sizing: border-box; margin: 0; padding: 0; }
  html, body { width: 1200px; height: 874px; overflow: hidden; }
  body {
    background: var(--bg);
    font-family: "Karla", Arial, sans-serif;
    position: relative;
  }
  .card {
    position: absolute;
    left: 280px;
    width: 640px;
    height: 366px;
    border-radius: 22px;
    overflow: hidden;
    box-shadow: 0 6px 18px rgba(0,0,0,.18);
  }
  .card--back { top: 40px; background: var(--brand-blue); }
  .card--front { top: 468px; background: var(--paper); }

  .back-mark {
    position: absolute;
    top: 140px; left: 0; right: 0;
    display: flex; align-items: center; justify-content: center; gap: 16px;
  }
  .back-mark__dot {
    width: 30px; height: 30px; border-radius: 50%;
    border: 4px solid var(--white);
  }
  .back-mark__name {
    font-family: "Cinzel", Georgia, serif;
    font-weight: 600; font-size: 40px; color: var(--white);
    letter-spacing: 1px;
  }
  .tagline {
    position: absolute; left: 40px; bottom: 36px;
    color: var(--white); font-size: 15px; letter-spacing: .3px;
  }

  .wave { position: absolute; inset: 0; }
  .company {
    position: absolute; top: 62px; left: 40px;
    font-family: "Cinzel", Georgia, serif;
    font-weight: 600; font-size: 30px; color: var(--navy);
    line-height: 1.15;
  }
  .contact {
    position: absolute; right: 36px; top: 218px;
    text-align: right; color: var(--white);
  }
  .contact__name {
    font-family: "Cinzel", Georgia, serif;
    font-weight: 600; font-size: 22px; letter-spacing: .5px;
    line-height: 1.2;
  }
  .contact__role {
    color: var(--accent-blue); font-size: 14px; line-height: 1.25;
    margin: 2px 0 6px;
  }
  .contact__line {
    display: flex; justify-content: flex-end; align-items: center; gap: 8px;
    font-size: 14px; line-height: 1.4;
  }
  .contact__icon { width: 13px; height: 13px; flex: none; }
</style>
</head>
<body>
  <section class="card card--back">
    <div class="back-mark">
      <span class="back-mark__dot"></span>
      <span class="back-mark__name">Callendry</span>
    </div>
    <p class="tagline">Proposals Management &amp; Capture support for complex procurements</p>
  </section>

  <section class="card card--front">
    <svg class="wave" viewBox="0 0 640 366" preserveAspectRatio="none" aria-hidden="true">
      <path d="M0 150 C 80 230, 170 290, 260 284 C 340 278, 390 168, 500 150 C 580 138, 625 160, 640 175 L640 366 L0 366 Z" fill="var(--accent-blue)"/>
      <path d="M0 162 C 80 242, 170 302, 260 296 C 340 290, 390 180, 500 162 C 580 150, 625 172, 640 187 L640 366 L0 366 Z" fill="var(--white)"/>
      <path d="M0 170 C 80 250, 170 310, 260 304 C 340 298, 390 188, 500 170 C 580 158, 625 180, 640 195 L640 366 L0 366 Z" fill="var(--navy)"/>
    </svg>

    <div class="company">Callendry<br>Advisory Group</div>

    <div class="contact">
      <p class="contact__name">NOEL FARDWICK</p>
      <p class="contact__role">Managing Director<br>Aerospace &amp; Defence</p>
      <p class="contact__line">438-261-7083
        <svg class="contact__icon" viewBox="0 0 16 16" aria-hidden="true"><path d="M3 1h3l1.5 4-2 1.3a9 9 0 0 0 4.2 4.2L11 8.5l4 1.5v3a2 2 0 0 1-2 2A13 13 0 0 1 1 3a2 2 0 0 1 2-2z" fill="var(--accent-blue)"/></svg>
      </p>
      <p class="contact__line">noel.fardwick@callendry.example
        <svg class="contact__icon" viewBox="0 0 16 16" aria-hidden="true"><rect x="1" y="3" width="14" height="10" rx="1.5" fill="var(--accent-blue)"/><path d="M1.5 4 8 9l6.5-5" stroke="var(--navy)" stroke-width="1.4" fill="none"/></svg>
      </p>
      <p class="contact__line">www.callendry.example
        <svg class="contact__icon" viewBox="0 0 16 16" aria-hidden="true"><circle cx="8" cy="8" r="7" fill="var(--accent-blue)"/><path d="M1 8h14M8 1c-3 3-3 11 0 14M8 1c3 3 3 11 0 14" stroke="var(--navy)" stroke-width="1.2" fill="none"/></svg>
      </p>
    </div>
  </section>
</body>
</html>
```